Consulting Company needs business card design

We need a business card design for a new consulting and business solutions company based in Bermuda called Corvale Partners Limited. Looking for a double sided business card with one side only including the company logo thats attached and the other including contact information. Logo contains blue and turquoise colors and is fine to be on both sides of the card.
Contact Information for Business Card
Corvale Partners Limited
P.O. Box HM318
Devonshire DV BX
Bermuda
Name: Marcus Pellegrin
Position: Director
Telephone: 1 441 733 4906
Email: mpellegrin@corvale.example
Website: www.corvale.example

```html
<!DOCTYPE html>
<html lang="en">
<head>
<meta charset="utf-8">
<title>Corvale Partners Limited – Business Card</title>
<link rel="stylesheet" href="https://fonts.googleapis.com/css2?family=Montserrat:wght@400;500;600&display=swap">
<style>
  :root {
    --sky: #26a9e1;
    --sky-deep: #1e9bd7;
    --teal: #14b1b5;
    --ink: #2b2b2b;
    --paper: #ffffff;
    --backdrop: #e6e8ea;
  }
  * { margin: 0; padding: 0; box-sizing: border-box; }
  html, body { width: 1200px; height: 930px; overflow: hidden; }
  body {
    background: var(--backdrop);
    font-family: "Montserrat", sans-serif;
    position: relative;
  }
  .card {
    position: absolute;
    left: 250px;
    width: 700px;
    height: 400px;
    border-radius: 22px;
    overflow: hidden;
    box-shadow: 0 6px 18px rgba(0,0,0,0.12);
  }
  .card--front { top: 40px; background: var(--sky); }
  .card--back { top: 490px; background: var(--paper); }

  .brand {
    position: absolute;
    display: flex;
    align-items: center;
    gap: 14px;
    font-weight: 600;
    white-space: nowrap;
  }
  .brand__dot { border-radius: 50%; flex: none; }

  .card--front .brand {
    left: 0; right: 0; top: 0; bottom: 0;
    justify-content: center;
    color: var(--paper);
    font-size: 34px;
  }
  .card--front .brand__dot { width: 46px; height: 46px; background: var(--paper); }

  .wave { position: absolute; inset: 0; width: 700px; height: 400px; }

  .card--back .brand {
    left: 60px; top: 200px;
    color: var(--sky);
    font-size: 24px;
  }
  .card--back .brand__dot { width: 40px; height: 40px; background: var(--teal); }

  .person {
    position: absolute;
    right: 52px; top: 176px;
    text-align: right;
  }
  .person__name {
    color: var(--sky);
    font-weight: 500;
    font-size: 26px;
    text-transform: uppercase;
    letter-spacing: 0.5px;
  }
  .person__role { color: var(--ink); font-size: 15px; margin-top: 2px; }

  .divider {
    position: absolute;
    left: 100px; right: 52px; top: 256px;
    height: 2px;
    background: var(--sky);
  }

  .address {
    position: absolute;
    right: 52px; top: 270px;
    text-align: right;
    color: var(--ink);
    font-size: 15px;
    line-height: 1.45;
  }
  .address__company { color: var(--sky); font-weight: 500; font-size: 17px; }

  .contact {
    position: absolute;
    left: 60px; top: 300px;
    list-style: none;
    color: var(--ink);
    font-size: 16px;
    line-height: 1.55;
  }
  .contact li { display: flex; align-items: center; gap: 12px; }
  .contact svg { width: 13px; height: 13px; flex: none; }
</style>
</head>
<body>

<section class="card card--front" aria-label="Card front">
  <div class="brand">
    <span class="brand__dot"></span>
    <span class="brand__name">Corvale Partners Limited</span>
  </div>
</section>

<section class="card card--back" aria-label="Card back">
  <svg class="wave" viewBox="0 0 700 400" aria-hidden="true">
    <path d="M0,0 H700 V78 C560,150 330,128 170,148 C90,158 35,178 0,200 Z" fill="var(--sky)"/>
    <path d="M0,200 C35,178 90,158 170,148 C330,128 560,150 700,78 V92 C560,166 330,142 172,162 C92,172 38,192 0,218 Z" fill="var(--teal)"/>
    <path d="M0,228 C40,202 95,182 175,172 C330,152 560,174 700,102 V106 C560,180 330,158 178,178 C98,188 42,210 0,238 Z" fill="var(--sky)"/>
  </svg>

  <div class="brand">
    <span class="brand__dot"></span>
    <span class="brand__name">Corvale Partners Limited</span>
  </div>

  <div class="person">
    <p class="person__name">Marcus Pellegrin</p>
    <p class="person__role">Director</p>
  </div>

  <div class="divider"></div>

  <address class="address">
    <p class="address__company">Corvale Partners Limited</p>
    <p>P.O. Box HM318</p>
    <p>Devonshire DV BX Bermuda</p>
  </address>

  <ul class="contact">
    <li>
      <svg viewBox="0 0 16 16" aria-hidden="true"><path d="M3 1h3l1.5 4-2 1.3a9 9 0 0 0 4.2 4.2L11 8.5l4 1.5v3a2 2 0 0 1-2 2A12 12 0 0 1 1 3a2 2 0 0 1 2-2z" fill="var(--sky)"/></svg>
      <span>1 441 733 4906</span>
    </li>
    <li>
      <svg viewBox="0 0 16 16" aria-hidden="true"><rect x="1" y="3" width="14" height="10" rx="1.5" fill="none" stroke="var(--sky)" stroke-width="1.6"/><path d="M1.5 4l6.5 5 6.5-5" fill="none" stroke="var(--sky)" stroke-width="1.6"/></svg>
      <span>mpellegrin@corvale.example</span>
    </li>
    <li>
      <svg viewBox="0 0 16 16" aria-hidden="true"><circle cx="8" cy="8" r="6.5" fill="none" stroke="var(--sky)" stroke-width="1.4"/><path d="M1.5 8h13M8 1.5c-3 3.5-3 9.5 0 13M8 1.5c3 3.5 3 9.5 0 13" fill="none" stroke="var(--sky)" stroke-width="1.2"/></svg>
      <span>www.corvale.example</span>
    </li>
  </ul>
</section>

</body>
</html>
```